Business Card Design Project

I need a business card design for an Organic drive thru coffee kiosk. We will serve organic coffee, teas & smoothies and will serve healthy breakfast food/snacks for people on the go.
I want the card to have 2-3 colors max (earthy colors like browns, greens and so on).
I have attached the logo I want used and would love to play off the theme of "balance."
Include:
Tidy-Kettle Coffee
address: 4820 Gorvin Ct. Raleigh, NC 27583
phone: 919-731-4062
website: www.tidy-kettle.com (website is not up yet but still include it on card)
email: Rosalind@tidy-kettle.com
I want one of the following sayings somewhere on the card (the front or back is fine):
"Eat & Drink Well, on the run!"
"Break the fast with Tidy-Kettle"
Maybe on the back list what we offer:
-Organic coffee, espresso & tea
-Blendora smoothies & protein shakes
-Zesty Pour (100% fresh local fruit and veggies)
-Tender Nibs

```html
<!DOCTYPE html>
<html lang="en">
<head>
<meta charset="utf-8">
<title>Tidy-Kettle Coffee — Business Card</title>
<link rel="stylesheet" href="https://fonts.googleapis.com/css2?family=Josefin+Sans:wght@400;600&display=swap">
<style>
  :root {
    --backdrop: #3e2717;
    --card-brown: #5d3914;
    --card-white: #ffffff;
    --cream: #e9ddc2;
    --roast: #5a3418;
    --bean-red: #9b4a38;
    --ink: #4a2c14;
  }
  html, body {
    margin: 0;
    padding: 0;
    overflow: hidden;
  }
  body {
    width: 1200px;
    height: 693px;
    background: var(--backdrop);
    position: relative;
    font-family: "Josefin Sans", sans-serif;
  }
  .card {
    position: absolute;
    top: 232px;
    width: 400px;
    height: 231px;
    box-shadow: 0 3px 10px rgba(0, 0, 0, 0.45);
  }
  .card--front {
    left: 149px;
    background: var(--card-brown);
  }
  .card--back {
    left: 648px;
    background: var(--card-white);
  }
  .brand {
    position: absolute;
    left: 0;
    right: 0;
    text-align: center;
  }
  .brand__dot {
    display: block;
    margin: 0 auto;
    border-radius: 50%;
    background: var(--bean-red);
  }
  .brand__name {
    display: block;
    font-weight: 600;
    line-height: 1;
  }
  .brand__tag {
    display: block;
    font-weight: 600;
    text-transform: uppercase;
  }
  .card--front .brand { top: 44px; }
  .card--front .brand__dot { width: 36px; height: 36px; margin-bottom: 16px; }
  .card--front .brand__name { font-size: 36px; color: var(--cream); letter-spacing: 0.3px; }
  .card--front .brand__tag { font-size: 9px; color: var(--cream); letter-spacing: 2px; margin-top: 12px; }

  .saying {
    position: absolute;
    left: 0;
    right: 0;
    top: 196px;
    margin: 0;
    text-align: center;
    font-size: 10px;
    letter-spacing: 1.2px;
    color: var(--cream);
    opacity: 0.8;
  }

  .card--back .brand { top: 38px; }
  .card--back .brand__dot { width: 26px; height: 26px; margin-bottom: 12px; }
  .card--back .brand__name { font-size: 25px; color: var(--roast); }
  .card--back .brand__tag { font-size: 7px; color: var(--bean-red); letter-spacing: 1.5px; margin-top: 5px; }

  .contact {
    position: absolute;
    left: 0;
    right: 0;
    color: var(--ink);
    font-size: 10px;
    letter-spacing: 2px;
  }
  .contact--address { top: 157px; }
  .contact--address .street { position: absolute; left: 30px; }
  .contact--address .phone { position: absolute; left: 274px; }
  .contact--online { top: 181px; text-align: center; letter-spacing: 1px; font-size: 9.5px; }
  .contact--online .email { margin-left: 18px; letter-spacing: 0.3px; }
  .band {
    position: absolute;
    left: 0;
    right: 0;
    top: 201px;
    height: 12px;
    background: var(--roast);
  }
</style>
</head>
<body>
  <section class="card card--front" aria-label="Card front">
    <div class="brand">
      <span class="brand__dot"></span>
      <span class="brand__name">Tidy-Kettle</span>
      <span class="brand__tag">Organic coffee + cafe</span>
    </div>
    <p class="saying">&ldquo;Break the fast with Tidy-Kettle&rdquo;</p>
  </section>

  <section class="card card--back" aria-label="Card back">
    <div class="brand">
      <span class="brand__dot"></span>
      <span class="brand__name">Tidy-Kettle</span>
      <span class="brand__tag">Organic coffee + cafe</span>
    </div>
    <div class="contact contact--address">
      <span class="street">4820 Gorvin Ct. Raleigh, NC 27583</span>
      <span class="phone">919-731-4062</span>
    </div>
    <div class="contact contact--online">
      <span class="web">www.tidy-kettle.com</span>
      <span class="email">Rosalind@tidy-kettle.com</span>
    </div>
    <div class="band"></div>
  </section>
</body>
</html>
```